Harbor SkyCare Global Air Ambulance Services
Harbor SkyCare Business Package
Harbor SkyCare Global Air Ambulance Services - Aerospace
Creative Brief
Professional
Mr. Doug Wilson Pratt
President / CEO
5273 West Dunmore Suite 410 Linden Falls, Oregon 85312-4706 United States of America
dpratt@harborskycare.example
http://www.harborskycare.example
jaxter42 jaxter42
Congratulations Morlund
vimal8marks vimal8marks
CH pls post feedback
HarborSkyCare HarborSkyCare
Looking away from any vertical formated cards
#191 - #194 - These pieces would be much more desirable if they were closer to our corporate colors: Again, please visit our website for reference: harborskycare.example
SiteAdmin SiteAdmin
Draft #160 by pario is a derivative of #119 by Tovesk, therefore has been taken down.
Draft #144 and its variation by bworkshopz are derivative of #119 by Tovesk, therefore have been taken down.
KDM27 KDM27
I was looking at your address and noticed I live about 5 minutes from there.... what a coincidence!
nanoGlyph nanoGlyph
please comment on my entry #129 and #131 thanks for your time nanoglyph
We love the punch out on #119
tinyrupa tinyrupa
wow alot of contestants, hehe.. i'm joining too in this project
minhcocoa minhcocoa
Thank you! Great comments!
First I want to begin by saying, “Thank you to everyone for participating”. Any ideas that we express are not meant to criticize or critique any designer(s). We simply want to allow you the ability to create “that piece that is just right” for our organization. 1.) I am not sure if maybe our in house design team has made the logo a little darker than the version I have uploaded: However, in order to get a good feeling of the corporate color, please visit our website; harborskycare.example: a. A good representation of what color we are looking for: #2 – The card in the upper right hand corner: On that card, we very much like the fade (bringing in more shadow towards the top ascending). b. Further, we also like the back of that card: 2.) The yellow / gold is too much & not what we are looking for: 3.) Many of the cards look like an “Insurance Identification Card”. 4.) #43 – We really like the drop shadow of the aircraft in the background: It also appears that there is a globe that is slightly visible – This looks very classy & exudes a first class service (This is image we are really trying to capture). 5.) #42 – We really like the shadow of the main portion of the logo 6.) #47 – The logo’s are all wrong: However, on what this person is portraying as the back of the card, the picture of the aircraft is sort of neat. The front of the card has WAY to much going on: 7.) We are most likely going to go with the rounded corners 8.) We are really liking the pictures on the card: Specifically, #57 & #58 captured our eye (with the picture positioning). 9.) We are looking for something that is very different from most business cards: We don’t want the same image for our organization 10.) Review our website for our companies colors: However, please don’t create anything that resembles “The sun burst” on the home page in the upper right hand corner (encompasses the words “Steady Wing Pledge”): We are not a fan of that any longer (I wasn’t a fan of that to begin with). I hope that some of this feedback will help everyone with a little better direction. Again, please understand that we are not trying to critique anyone (everyone has different tastes & we recognize that). Thank you for you for all of your efforts.

```html
<!DOCTYPE html>
<html lang="en">
<head>
<meta charset="utf-8">
<title>Harbor SkyCare Business Package</title>
<link rel="stylesheet" href="https://fonts.googleapis.com/css2?family=Open+Sans:wght@400;700&display=swap">
<style>
  :root {
    --board: #5a4f45;
    --paper-light: #f1eee8;
    --paper-mid: #dcd6cc;
    --paper-dark: #bdb4a7;
    --taupe: #9a8f80;
    --burgundy: #6b1a24;
    --burgundy-deep: #4f1019;
    --ink: #4a4038;
    --ink-soft: #7a7066;
  }
  * { box-sizing: border-box; margin: 0; padding: 0; }
  html, body { width: 1200px; height: 871px; overflow: hidden; }
  body {
    background: var(--board);
    font-family: "Open Sans", Arial, sans-serif;
    position: relative;
  }
  .piece {
    position: absolute;
    background: linear-gradient(160deg, var(--paper-dark) 0%, var(--paper-light) 35%, var(--paper-mid) 60%, var(--paper-light) 80%, var(--paper-dark) 100%);
    box-shadow: 3px 4px 10px rgba(0,0,0,.35);
    overflow: hidden;
  }
  .swoosh { position: absolute; left: 0; bottom: 0; width: 100%; }

  .brand { position: absolute; display: flex; align-items: center; gap: 6px; }
  .brand-mark { background: var(--burgundy); }
  .brand-name { color: var(--burgundy); font-weight: 700; line-height: 1; white-space: nowrap; }
  .brand-tag { position: absolute; color: var(--ink-soft); font-size: 4px; letter-spacing: .5px; text-transform: uppercase; white-space: nowrap; }

  .letterhead { left: 115px; top: 101px; width: 418px; height: 660px; }
  .letterhead .brand { left: 30px; top: 34px; }
  .letterhead .brand-mark { width: 12px; height: 12px; }
  .letterhead .brand-name { font-size: 15px; }
  .letterhead .brand-tag { left: 48px; top: 53px; }
  .contact-block { position: absolute; right: 30px; top: 36px; text-align: right; font-size: 4.5px; line-height: 1.6; color: var(--ink-soft); white-space: nowrap; }

  .envelope-front { left: 600px; top: 113px; width: 461px; height: 225px; }
  .envelope-front .brand { left: 18px; top: 22px; }
  .envelope-front .brand-mark { width: 10px; height: 10px; }
  .envelope-front .brand-name { font-size: 12px; }
  .envelope-front .brand-tag { left: 34px; top: 37px; }
  .envelope-front .contact-block { right: 18px; top: 24px; font-size: 4px; }

  .envelope-back { left: 600px; top: 355px; width: 461px; height: 226px; }
  .flap-band {
    position: absolute; left: 0; top: 0; width: 100%; height: 36px;
    background: linear-gradient(180deg, var(--burgundy-deep), var(--burgundy));
  }
  .flap-seal { position: absolute; left: 50%; top: 50%; width: 12px; height: 12px; margin: -6px 0 0 -6px; border-radius: 50%; background: var(--paper-light); opacity: .85; }

  .card { top: 617px; width: 247px; height: 146px; border-radius: 10px; }
  .card-front { left: 583px; }
  .card-front .brand { left: 16px; top: 20px; }
  .card-front .brand-mark { width: 10px; height: 10px; }
  .card-front .brand-name { font-size: 12px; }
  .card-front .brand-tag { left: 32px; top: 35px; }
  .aircraft-shadow {
    position: absolute; left: 30px; top: 56px; width: 150px; height: 50px;
    background: radial-gradient(ellipse at center, rgba(150,140,128,.45), rgba(150,140,128,0) 70%);
  }
  .card-web { position: absolute; left: 20px; top: 108px; font-size: 4.5px; color: var(--ink-soft); white-space: nowrap; }

  .card-back { left: 845px; }
  .card-back .brand { right: 14px; top: 16px; gap: 4px; }
  .card-back .brand-mark { width: 8px; height: 8px; }
  .card-back .brand-name { font-size: 9px; }
  .person { position: absolute; left: 16px; top: 16px; color: var(--ink); }
  .person-name { font-size: 5.5px; font-weight: 700; white-space: nowrap; }
  .person-title { font-size: 4.2px; color: var(--ink-soft); margin-top: 1px; }
  .portrait {
    position: absolute; left: 16px; top: 36px; width: 58px; height: 80px;
    background: linear-gradient(180deg, #d9d6d0 0%, #a09a92 55%, #2a2624 100%);
  }
  .person-details { position: absolute; left: 92px; top: 40px; font-size: 4.2px; line-height: 1.7; color: var(--ink-soft); white-space: nowrap; }
</style>
</head>
<body>

<section class="piece letterhead" aria-label="Letterhead">
  <div class="brand"><span class="brand-mark"></span><span class="brand-name">Harbor SkyCare</span></div>
  <div class="brand-tag">Global Air Ambulance Services</div>
  <div class="contact-block">
    5273 West Dunmore Suite 410<br>
    Linden Falls, Oregon 85312-4706<br>
    Tel 555 010 0142<br>
    http://www.harborskycare.example
  </div>
  <svg class="swoosh" viewBox="0 0 418 110" height="110" preserveAspectRatio="none">
    <defs>
      <linearGradient id="lhFill" x1="0" y1="0" x2="1" y2="0">
        <stop offset="0" stop-color="#8f8475"/>
        <stop offset=".5" stop-color="#c9c1b5"/>
        <stop offset="1" stop-color="#a69b8c"/>
      </linearGradient>
    </defs>
    <path d="M0 40 C120 95 280 95 418 20 L418 110 L0 110 Z" fill="url(#lhFill)"/>
    <path d="M0 30 C130 90 290 88 418 12" fill="none" stroke="var(--burgundy)" stroke-width="1"/>
    <path d="M0 44 C140 100 300 96 418 28" fill="none" stroke="#ece7df" stroke-width="1.2"/>
  </svg>
</section>

<section class="piece envelope-front" aria-label="Envelope front">
  <div class="brand"><span class="brand-mark"></span><span class="brand-name">Harbor SkyCare</span></div>
  <div class="brand-tag">Global Air Ambulance Services</div>
  <div class="contact-block">
    5273 West Dunmore Suite 410<br>
    Linden Falls, Oregon 85312-4706
  </div>
  <svg class="swoosh" viewBox="0 0 461 70" height="70" preserveAspectRatio="none">
    <defs>
      <linearGradient id="efFill" x1="0" y1="0" x2="1" y2="0">
        <stop offset="0" stop-color="#8f8475"/>
        <stop offset=".5" stop-color="#c9c1b5"/>
        <stop offset="1" stop-color="#a69b8c"/>
      </linearGradient>
    </defs>
    <path d="M0 30 C150 70 320 65 461 14 L461 70 L0 70 Z" fill="url(#efFill)"/>
    <path d="M0 22 C150 64 320 58 461 6" fill="none" stroke="var(--burgundy)" stroke-width="1"/>
    <path d="M0 34 C160 72 330 66 461 20" fill="none" stroke="#ece7df" stroke-width="1"/>
  </svg>
</section>

<section class="piece envelope-back" aria-label="Envelope back">
  <div class="flap-band"><span class="flap-seal"></span></div>
  <svg class="swoosh" viewBox="0 0 461 60" height="60" preserveAspectRatio="none">
    <path d="M0 26 C150 60 320 56 461 12 L461 60 L0 60 Z" fill="#a89d8e" opacity=".7"/>
    <path d="M0 20 C150 56 320 50 461 6" fill="none" stroke="var(--burgundy)" stroke-width="1"/>
  </svg>
</section>

<section class="piece card card-front" aria-label="Business card front">
  <div class="aircraft-shadow" role="img" aria-label="Faint shadow of an air ambulance aircraft over a globe"></div>
  <div class="brand"><span class="brand-mark"></span><span class="brand-name">Harbor SkyCare</span></div>
  <div class="brand-tag">Global Air Ambulance Services</div>
  <div class="card-web">http://www.harborskycare.example</div>
  <svg class="swoosh" viewBox="0 0 247 40" height="40" preserveAspectRatio="none">
    <path d="M0 22 C80 42 170 38 247 8 L247 40 L0 40 Z" fill="#a89d8e" opacity=".8"/>
    <path d="M0 16 C80 38 170 34 247 3" fill="none" stroke="var(--burgundy)" stroke-width=".8"/>
  </svg>
</section>

<section class="piece card card-back" aria-label="Business card back">
  <div class="person">
    <div class="person-name">Mr. Doug Wilson Pratt</div>
    <div class="person-title">President / CEO</div>
  </div>
  <div class="brand"><span class="brand-mark"></span><span class="brand-name">Harbor SkyCare</span></div>
  <div class="portrait" role="img" aria-label="Portrait photograph of the company president"></div>
  <div class="person-details">
    5273 West Dunmore Suite 410<br>
    Linden Falls, Oregon 85312-4706<br>
    United States of America<br>
    Tel 555 010 0142<br>
    Fax 555 010 0143<br>
    dpratt@harborskycare.example
  </div>
  <svg class="swoosh" viewBox="0 0 247 40" height="40" preserveAspectRatio="none">
    <path d="M0 22 C80 42 170 38 247 8 L247 40 L0 40 Z" fill="#a89d8e" opacity=".8"/>
    <path d="M0 16 C80 38 170 34 247 3" fill="none" stroke="var(--burgundy)" stroke-width=".8"/>
  </svg>
</section>

</body>
</html>
```